Quarvella Brochure Design - IT Services - Modern Design - Services List

Hi,

We are looking for a modern IT Services brochure design of between 4 - 6 pages, it must be based on a blue and white colour theme with some nice technical imagery. It would need a section about why Quarvella and a contact section at the end.

Here is some info that could be included

Target Market(s)

Medium to Large Businesses

Industry/Entity Type

Information Technology

Colors
0054AA
0677BA
7BADD7
CADEEF
E8F1F8

Requirements
Must have
• Striking technical imagery
Nice to have
• Nice Icons to list the different services sections

```html
<!DOCTYPE html>
<html lang="en">
<head>
<meta charset="utf-8">
<title>Quarvella – Why Choose Us</title>
<link href="https://fonts.googleapis.com/css2?family=Poppins:wght@400;500;600;700&display=swap" rel="stylesheet">
<style>
  :root{
    --brand-blue:#1255a6;
    --card-blue:#0677ba;
    --ink-blue:#0f4fa3;
    --text-grey:#444a52;
    --white:#ffffff;
  }
  *{margin:0;padding:0;box-sizing:border-box;}
  html,body{width:1200px;height:848px;overflow:hidden;background:var(--white);}
  body{font-family:'Poppins',sans-serif;text-transform:uppercase;}
  .brochure{position:relative;width:1200px;height:848px;overflow:hidden;background:var(--white);}
  .layer{position:absolute;left:0;top:0;}

  .why-title{position:absolute;left:54px;top:664px;color:var(--white);font-weight:600;font-size:40px;line-height:41px;letter-spacing:1.5px;}

  .reason{position:absolute;left:436px;width:305px;height:106px;padding:14px 10px 0 24px;}
  .reason--outline{border:1.5px solid var(--card-blue);border-radius:0 16px 0 16px;background:var(--white);}
  .reason--filled{background:var(--card-blue);border-radius:16px 0 16px 0;}
  .reason__title{position:relative;font-weight:500;font-size:11.5px;letter-spacing:.4px;color:var(--ink-blue);margin-bottom:6px;}
  .reason__title::before{content:"";position:absolute;left:-8px;top:2px;width:2.5px;height:11px;background:currentColor;}
  .reason__text{font-size:8.7px;line-height:12px;letter-spacing:.3px;color:var(--text-grey);}
  .reason--filled .reason__title,.reason--filled .reason__text{color:var(--white);}

  .touch-pill{position:absolute;left:400px;top:714px;width:221px;height:25px;background:var(--white);border-radius:0 13px 13px 0;}
  .touch-pill h2{position:absolute;left:44px;top:-1px;font-weight:600;font-size:20.5px;color:var(--ink-blue);letter-spacing:.5px;}
  .touch-text{position:absolute;left:444px;top:755px;width:290px;color:var(--white);font-size:8.7px;line-height:12px;letter-spacing:.3px;}

  .contact-card{position:absolute;left:884px;top:344px;width:265px;height:453px;background:var(--white);border-radius:46px;text-align:center;}
  .contact-card h3{font-weight:600;font-size:15.5px;color:var(--ink-blue);display:inline-block;border-bottom:1.5px solid var(--ink-blue);padding-bottom:1px;letter-spacing:.4px;}
  .contact-head{position:absolute;left:0;right:0;}
  .contact-item{position:absolute;left:0;right:0;}
  .contact-item dt{font-weight:500;font-size:12.5px;color:var(--ink-blue);line-height:16px;letter-spacing:.4px;}
  .contact-item dd{font-size:11.5px;color:var(--text-grey);line-height:15.5px;letter-spacing:.3px;}
  .social{position:absolute;left:0;right:0;top:398px;display:flex;justify-content:center;gap:16px;}
  .social span{width:20px;height:20px;border-radius:50%;background:var(--ink-blue);display:block;}
</style>
</head>
<body>
<div class="brochure">

  <!-- left panel -->
  <svg class="layer" width="360" height="848" viewBox="0 0 360 848">
    <defs>
      <linearGradient id="warmTone" x1="0" y1="0" x2="1" y2="1">
        <stop offset="0" stop-color="#eeeae4"/>
        <stop offset=".45" stop-color="#b08a66"/>
        <stop offset="1" stop-color="#8a6a4c"/>
      </linearGradient>
    </defs>
    <path d="M0,6 H351 V595 H80 Q28,592 0,568 Z" fill="url(#warmTone)" role="img" aria-label="Photo of a smiling woman on the phone taking notes at a desk"/>
    <path d="M0,576 Q32,602 82,603 H355 V848 H0 Z" fill="var(--brand-blue)"/>
  </svg>
  <h1 class="why-title">Why<br>Choose<br>Quarvella?</h1>

  <!-- middle column -->
  <article class="reason reason--outline" style="top:52px">
    <h2 class="reason__title">Expertise and Experience</h2>
    <p class="reason__text">With years of experience in the IT industry, our team possesses the knowledge and skills to tackle any challenge. We stay abreast of the latest technological advancements to provide you with cutting-edge solutions.</p>
  </article>
  <article class="reason reason--filled" style="top:201px">
    <h2 class="reason__title">Customer-Centric Approach</h2>
    <p class="reason__text">We prioritize our clients' needs and work closely with them to deliver customized solutions that drive success. Our client-centric approach ensures that we are always aligned with your business goals.</p>
  </article>
  <article class="reason reason--outline" style="top:350px">
    <h2 class="reason__title">Proactive Support</h2>
    <p class="reason__text">Our proactive support model ensures that potential issues are identified and resolved before they can impact your operations. We are committed to maintaining the highest levels of service availability and performance.</p>
  </article>
  <article class="reason reason--filled" style="top:500px">
    <h2 class="reason__title">Comprehensive Solutions</h2>
    <p class="reason__text">From managed services to cybersecurity, we offer a comprehensive suite of IT solutions designed to meet the diverse needs of your business. Our holistic approach ensures that all aspects of your IT infrastructure are covered.</p>
  </article>

  <!-- blue bands middle + right -->
  <svg class="layer" width="1200" height="848" viewBox="0 0 1200 848">
    <defs>
      <linearGradient id="officeTone" x1="0" y1="0" x2="1" y2="1">
        <stop offset="0" stop-color="#f2f0ee"/>
        <stop offset=".5" stop-color="#d9d4cf"/>
        <stop offset=".75" stop-color="#5f86c7"/>
        <stop offset="1" stop-color="#9a7456"/>
      </linearGradient>
    </defs>
    <path d="M400,848 V713 Q400,653 462,653 H859 V848 Z" fill="var(--brand-blue)"/>
    <rect x="859" y="300" width="341" height="548" fill="var(--brand-blue)"/>
    <path d="M859,0 H1200 V352 Q1196,404 1150,408 H910 Q864,404 859,366 Z" fill="url(#officeTone)" role="img" aria-label="Photo of a woman working at a desktop computer in an office"/>
  </svg>

  <div class="touch-pill"><h2>Get in Touch</h2></div>
  <p class="touch-text">Discover how Quarvella can transform your IT landscape and drive your business forward. Contact us today to learn more about our services and how we can help you achieve your goals.</p>

  <!-- contact card -->
  <section class="contact-card">
    <div class="contact-head" style="top:69px"><h3>Contact Us</h3></div>
    <dl>
      <div class="contact-item" style="top:110px"><dt>Phone</dt><dd>+44 120 555 0147</dd></div>
      <div class="contact-item" style="top:157px"><dt>Website</dt><dd>www.quarvella.co.uk</dd></div>
      <div class="contact-item" style="top:206px"><dt>Email</dt><dd>info@quarvella.co.uk</dd></div>
      <div class="contact-item" style="top:255px"><dt>Address</dt><dd>45 Harbour Lane, Northgate<br>Park, London, UK</dd></div>
    </dl>
    <div class="contact-head" style="top:359px"><h3>Follow Us</h3></div>
    <div class="social">
      <span aria-label="Social profile one"></span>
      <span aria-label="Social profile two"></span>
      <span aria-label="Social profile three"></span>
    </div>
  </section>

</div>
</body>
</html>
```